Occasions chocolate packaging

We are looking for 7 packaging designs for bars of chocolate.

Each design needs to be different and we’re not looking for a consistent brand or branding message across the designs. Inspiration should come from gift/occasion cards. Fun, simple, bold, vibrant colours and eye catching, i.e. not vintage or just text.

The front of the packaging should have the main message on and is free of any branding. You don’t need to design the back, just simply allow the main background colour or design pattern to continue around.

These are the different designs we are after, I’ve added in some text for each to give you some guidance but feel free to play around with the message if it suits the design better.

1) Mum
‘The best mum’, ‘Best mum in the World’, ‘Number 1 Mum’

2) Dad
‘The Best Dad’, ‘Best Dad Ever’, ‘Number 1 Dad’, ‘You’re my hero Dad’

3) Husband
‘Best Husband in the World’, ‘Husband I Love You’, ‘Darling Husband’

4) Wife
‘Best Wife in the World’, ‘For my Wonderful Wife’, ‘My Beautiful Wife’

5) Congratulations
Simple one, just Congratulations

6) Thinking of you
Try and keep this neutral as it could be used for happy and sad situations.

7) Thank you
Keep this gender neutral.

Sides:
The sides need to have the following text:

FINE BELGIAN DARK CHOCOLATE
infused with Orange

Back:
The main colour of the front should continue all the way around, we will place a box with the contents and bar code on here ourselves so no need to do anything.

Dimensions:
Attached in the document, front of package is 85mm by 190mm.

The packaging is made from folded card, the first blank part is for gluing the back on to.

Reason: I'm extending the deadline as I've only received 1 design so far which has followed the brief. Although I do like it, I would like to see at least some competition...

```html
<!DOCTYPE html>
<html lang="en">
<head>
<meta charset="utf-8">
<title>Best Mum in the World – Chocolate Bar Front</title>
<link rel="stylesheet" href="https://fonts.googleapis.com/css2?family=Oswald:wght@600;700&family=Josefin+Sans:wght@600;700&display=swap">
<style>
  :root {
    --page: #e9e9e9;
    --pink: #e8176f;
    --pink-light: #f23d8c;
    --pink-deep: #c8105c;
    --band: #b30d52;
    --band-edge: #d4206c;
    --figure-soft: #f7c6dc;
    --white: #ffffff;
  }
  * { margin: 0; padding: 0; box-sizing: border-box; }
  html, body {
    width: 1200px;
    height: 960px;
    overflow: hidden;
    background: var(--page);
  }
  .canvas {
    width: 1200px;
    height: 960px;
    display: flex;
    align-items: center;
    justify-content: center;
  }
  .bar-front {
    width: 390px;
    height: 872px;
    background: linear-gradient(160deg, var(--pink-light) 0%, var(--pink) 45%, var(--pink-deep) 100%);
    overflow: hidden;
    display: flex;
    flex-direction: column;
    align-items: center;
  }
  .hero-illustration {
    flex: none;
    margin-top: 40px;
    width: 240px;
    height: 330px;
    border-radius: 6px;
    background: radial-gradient(ellipse at 50% 40%, var(--white) 0%, var(--figure-soft) 70%, rgba(247,198,220,0.3) 100%);
  }
  .headline {
    flex: none;
    margin-top: 16px;
    font-family: "Oswald", sans-serif;
    font-weight: 700;
    color: var(--white);
    text-transform: uppercase;
    text-align: center;
    line-height: 0.95;
    letter-spacing: -1px;
  }
  .headline .line-best,
  .headline .line-mum { display: block; font-size: 100px; }
  .headline .line-world {
    display: block;
    font-size: 46px;
    letter-spacing: -1px;
    margin-top: 6px;
  }
  .flavour-band {
    flex: none;
    margin-top: auto;
    width: 100%;
    height: 190px;
    background: var(--band);
    border-top: 2px solid var(--band-edge);
    display: flex;
    flex-direction: column;
    align-items: center;
    justify-content: center;
    font-family: "Josefin Sans", sans-serif;
    font-weight: 700;
    color: var(--white);
    text-transform: uppercase;
    text-align: center;
  }
  .flavour-band .range { font-size: 34px; line-height: 1.1; letter-spacing: 2px; }
  .flavour-band .infusion { font-size: 22px; letter-spacing: 3px; margin-top: 10px; font-weight: 600; }
</style>
</head>
<body>
  <main class="canvas">
    <section class="bar-front">
      <div class="hero-illustration" role="img" aria-label="White silhouette of a mother bending down to her young daughter, both holding a pink heart"></div>
      <h1 class="headline">
        <span class="line-best">Best</span>
        <span class="line-mum">Mum</span>
        <span class="line-world">In the World</span>
      </h1>
      <div class="flavour-band">
        <p class="range">Fine Belgian<br>Dark Chocolate</p>
        <p class="infusion">Infused with Orange</p>
      </div>
    </section>
  </main>
</body>
</html>
```